Dane Morrow films- wedding and event films company website. DESKTOP AND MOBILE

We need a website for a high-end wedding and event film production company. Looking for a very modern and elegant design. my old website is www.danemorrowfilms.example

I like the "white/black/rose gold" color scheme of my logo.

really looking for a sleek modern design the breaths professional and artistic.

Target Market(s)

wedding and event films.

Industry/Entity Type

Film Production

Number of Pages Required

5+ page

Colors

Designer to choose colors to be used in the design.

Requirements
Must have
• website name will be www.danemorrowfilms.example
• tagline is "CINEMATIC STORIES ABOUT YOU"
• sections: HOME, CONTACT, ABOUT, FILMS, BLOG
• You can see my old website at danemorrowfilms.example
• Website about section:
• Dane Morrow Films was Established with the basis of truly cinematic and artistic films in mind. Dane and his team routinely travel the globe documenting weddings and events for high profile clients and discerning couples. Dane was born and raised in Maui Hawaii and has a unique approach to his films that embody the essence of a Hollywood film. Dane has spent the last 10 years traveling the world documenting corporate events and weddings with multiple Award winning production companies. In 2017 Dane decided to establish his own brand “Dane Morrow films” that will take everything he has learned with his past experiences and push it to the next level. Aside from his personal achievements, Dane is extremely passionate about his craft and always looks forward to handcrafting beautiful wedding/event films for his clients. The style of work is non-traditional and the day of filming is extremely unobtrusive (as we are looking for natural-candid/ raw emotions).
• If you are looking for the best price in town, we are probably not the best option, but if you’re looking for the best quality and peace of mind on your wedding day, then you’re in the right place. Dane Morrow Films is a boutique studio that only accepts a limited number of assignments per year. Inquire early to ensure availability.
• LINKS TO VIMEO VIDEOS THAT WILL BE IN THE "FILMS' SECTION.
• BRENT FILM TRAILER - https://clipvault.example/508114362
• BRENT FEATURE FILM - https://clipvault.example/617392048
• JUNE AND ROB'S WEDDING - https://clipvault.example/724958160
• DRONE DEMO REEL - https://clipvault.example/841576203
• WEDDING INDUSTRY EVENT PARTY - https://clipvault.example/962304817/a8d3e7b21c
• images that you can use on site are here: https://brigittolsenimages.proofbox.example/gallery/nora&felix/
• password is: meadow

```html
<!DOCTYPE html>
<html lang="en">
<head>
<meta charset="utf-8">
<title>Dane Morrow Films — Cinematic Stories About You</title>
<link rel="stylesheet" href="https://fonts.googleapis.com/css2?family=Lato:wght@300;400;700;900&display=swap">
<style>
:root{
  --accent:#dc8f55;
  --accent-dark:#b9713d;
  --ink:#222222;
  --body:#444444;
  --muted:#8a8a8a;
  --line:#d9d9d9;
  --paper:#ffffff;
  --stone:#efece6;
  --night:#1c1a18;
}
*{box-sizing:border-box;margin:0;padding:0}
html,body{width:1200px;height:3846px;overflow:hidden}
body{font-family:"Lato",sans-serif;color:var(--body);background:var(--paper);position:relative}
section,header,footer{position:absolute;left:0;width:1200px}
.abs{position:absolute}
.btn{display:inline-block;background:var(--accent);color:#fff;font-family:"Lato",sans-serif;font-weight:700;font-size:14px;letter-spacing:.5px;text-transform:uppercase;padding:11px 18px;border:none}
.btn-outline{background:transparent;border:2px solid rgba(255,255,255,.8);color:#fff}
.section-title{position:absolute;left:0;width:1200px;text-align:center;font-weight:900;font-size:30px;letter-spacing:1px;color:var(--ink);text-transform:uppercase}
.section-title span{color:var(--accent)}
.rule{position:absolute;height:1px;background:var(--line)}

/* Header */
.site-header{top:0;height:123px;background:var(--paper)}
.brand{left:141px;top:50px;display:flex;align-items:center;gap:12px;font-weight:700;font-size:22px;letter-spacing:1.5px;color:var(--ink)}
.brand-mark{width:16px;height:16px;background:var(--accent)}
.main-nav{left:562px;top:74px;display:flex;align-items:center}
.main-nav a{font-size:13px;font-weight:700;color:var(--ink);text-decoration:none;letter-spacing:.5px;padding:0 28px;border-left:1px solid var(--line)}
.main-nav a:first-child{border-left:none;color:var(--accent)}

/* Hero */
.hero{top:123px;height:518px}
.hero-photo{position:absolute;inset:0;background:linear-gradient(100deg,#2c3a22 0%,#4d5a33 35%,#9a8a77 60%,#a07a95 75%,#6b5b4c 100%)}
.hero-box{left:133px;top:169px;width:436px;height:241px;border:2px solid rgba(255,255,255,.85);background:rgba(20,20,20,.35);text-align:center;padding-top:82px}
.hero-box h1{color:#fff;font-weight:400;font-size:32px;line-height:42px;letter-spacing:.5px}
.hero-box .btn{margin-top:14px}

/* About */
.about{top:641px;height:626px}
.about-photo{left:133px;top:72px;width:449px;height:487px;border:6px solid #f2f2f2;box-shadow:0 0 0 1px #ddd;background:linear-gradient(160deg,#bdbdbd,#4a4a4a)}
.about-body{left:623px;top:62px;width:444px}
.about-body h2{font-weight:900;font-size:30px;color:var(--ink)}
.about-body h2 span{color:var(--accent)}
.about-body .rule-inline{height:1px;background:var(--line);margin:30px 0 34px}
.about-body p{font-size:13.5px;line-height:26px;color:var(--body);text-align:justify}
.about-body h3{color:var(--accent);font-weight:700;font-size:16px;margin:12px 0 8px}
.about-body .btn{margin-top:18px}

/* Quote */
.quote{top:1267px;height:241px;background:linear-gradient(180deg,#e8a56f 0%,#d38b55 55%,#b9733f 100%);text-align:center;color:#fff}
.quote blockquote{position:absolute;left:200px;top:54px;width:800px;font-weight:300;font-size:29px;line-height:40px}
.quote cite{position:absolute;left:0;top:140px;width:1200px;font-style:normal;font-weight:700;font-size:23px}

/* Films */
.films{top:1508px;height:564px;background:var(--stone)}
.film{top:176px;width:446px;height:252px}
.film-frame{position:absolute;inset:0}
.film-1 .film-frame{background:linear-gradient(180deg,#2a1a14 0%,#6e4a2a 40%,#2b7c8a 70%,#182022 100%)}
.film-2 .film-frame{background:linear-gradient(180deg,#b8c7d2 0%,#8aa07a 45%,#d5d2c6 75%,#6c6a62 100%)}
.film-controls{position:absolute;left:0;bottom:0;width:100%;height:34px;background:rgba(0,0,0,.55);display:flex;align-items:center;gap:12px;padding:0 12px}
.film-controls .bar{flex:1;height:6px;background:rgba(255,255,255,.35)}
.film-controls .bar i{display:block;width:12%;height:100%;background:#2fa9d8}
.film-side{position:absolute;right:8px;top:8px;width:26px;display:flex;flex-direction:column;gap:6px}
.film-side i{display:block;height:22px;background:rgba(20,20,20,.7);border-radius:3px}
.dots{left:576px;top:494px;display:flex;gap:6px}
.dots i{width:8px;height:5px;border-radius:3px;background:#e3b795}
.dots i.on{width:16px;background:var(--accent)}

/* CTA */
.cta{top:2133px;height:359px}
.cta-photo{position:absolute;inset:0;background:linear-gradient(100deg,#0c1822 0%,#103a4e 30%,#2a9fc0 50%,#c9a77a 70%,#3b2a1c 100%)}
.cta-box{left:133px;top:59px;width:464px;height:231px;background:rgba(15,15,15,.85);border:1px solid rgba(255,255,255,.15);padding:38px 40px}
.cta-box p{color:#fff;font-size:19px;line-height:31px}
.cta-box .btn{margin-top:20px}

/* Blog */
.blog{top:2492px;height:621px}
.post{top:175px;width:295px;height:366px;border:1px solid #e2e2e2;background:#fff}
.post-photo{height:185px}
.post-1 .post-photo{background:linear-gradient(160deg,#6b4a3c,#d8c7b2)}
.post-2 .post-photo{background:linear-gradient(160deg,#6e7b86,#c7b9a2)}
.post-3 .post-photo{background:linear-gradient(160deg,#5d7a42,#cfc2a6)}
.post-body{padding:16px 16px 0}
.post-body h4{font-size:15px;font-weight:700;color:var(--ink)}
.post-meta{font-size:11.5px;color:var(--muted);margin:7px 0 9px}
.post-body p{font-size:13px;line-height:20px;color:var(--body)}
.post-body .btn{margin-top:16px;font-size:12px;padding:9px 14px}
.arrow{top:327px}

/* Contact */
.contact{top:3113px;height:674px;background:linear-gradient(180deg,#2a2623 0%,#3b2f25 60%,#241e19 100%)}
.contact .section-title{color:#fff;top:56px}
.contact-panel{left:236px;top:200px;width:728px;height:405px;background:rgba(170,110,65,.72)}
.contact-icon{left:568px;top:176px;width:58px;height:58px;border-radius:50%;background:#fff}
.contact-info{position:absolute;left:0;top:66px;width:100%;text-align:center;color:#fff;font-size:14px;line-height:25px}
.field{position:absolute;background:#f3ede8;font-size:11px;color:#555;padding:9px 10px}
.contact-panel .btn{position:absolute;left:275px;top:325px;font-size:12px;padding:10px 18px}

/* Footer */
.site-footer{top:3787px;height:59px;background:var(--night);color:#fff;font-size:12px;text-align:center;line-height:59px}
</style>
</head>
<body>

<header class="site-header">
  <div class="abs brand"><span class="brand-mark"></span>DANE MORROW FILMS</div>
  <nav class="abs main-nav">
    <a href="#home">HOME</a><a href="#about">ABOUT</a><a href="#films">FILMS</a><a href="#blog">BLOG</a><a href="#contact">CONTACT</a>
  </nav>
</header>

<section class="hero" id="home">
  <div class="hero-photo" role="img" aria-label="Two young bridesmaids holding bouquets walking down garden steps"></div>
  <div class="abs hero-box">
    <h1>CINEMATIC<br>STORIES ABOUT YOU</h1>
    <span class="btn">Book your wedding or event now !</span>
  </div>
</section>

<section class="about" id="about">
  <div class="abs about-photo" role="img" aria-label="Black and white portrait of the filmmaker"></div>
  <div class="abs about-body">
    <h2>ABOUT <span>US</span></h2>
    <div class="rule-inline"></div>
    <p>At Dane Morrow Films we specialize in offering the finest in wedding and corporate cinematography. We offer a very modern and creative style for capturing your special moments with a beautiful and cinematic approach that enables up to produce the highest quality of films. Dane and his hand selected team have over 10 years of experience, and they strive to make the best films in the industry. We pride ourselves on remaining attentive to clients' needs, business practices rooted in integrity, and continually striving to be at the forefront of innovation in our industry.</p>
    <h3>The Cinematic Difference</h3>
    <p>We pride ourselves on using the best quality cinema tools for our films. The equipment we use are industry standard cinematic tools used in hollywood movies, using such tools gives our films a truely cinematic feel.</p>
    <span class="btn">Read more</span>
  </div>
</section>

<section class="quote">
  <blockquote>"Dane really is one of the best film makers in Hawaii, great work Dane! We loved the film!"</blockquote>
  <cite>— Lena Harlow</cite>
</section>

<section class="films" id="films">
  <h2 class="section-title" style="top:60px">FILMS</h2>
  <div class="rule" style="left:133px;top:128px;width:934px"></div>
  <div class="abs film film-1" style="left:133px">
    <div class="film-frame" role="img" aria-label="Wedding reception in a chandelier ballroom lit in teal and pink"></div>
    <div class="film-side"><i></i><i></i><i></i><i></i></div>
    <div class="film-controls">
      <svg width="12" height="14" viewBox="0 0 12 14"><path d="M0 0L12 7L0 14Z" fill="#fff"/></svg>
      <div class="bar"><i></i></div>
      <svg width="14" height="14" viewBox="0 0 14 14"><path d="M0 0h5v2H2v3H0zM14 0v5h-2V2H9V0zM0 14V9h2v3h3v2zM14 14H9v-2h3V9h2z" fill="#fff"/></svg>
    </div>
  </div>
  <div class="abs film film-2" style="left:621px">
    <div class="film-frame" role="img" aria-label="Outdoor wedding ceremony with guests seated on a lawn"></div>
    <div class="film-side"><i></i><i></i><i></i><i></i></div>
    <div class="film-controls">
      <svg width="12" height="14" viewBox="0 0 12 14"><path d="M0 0L12 7L0 14Z" fill="#fff"/></svg>
      <div class="bar"><i></i></div>
      <svg width="14" height="14" viewBox="0 0 14 14"><path d="M0 0h5v2H2v3H0zM14 0v5h-2V2H9V0zM0 14V9h2v3h3v2zM14 14H9v-2h3V9h2z" fill="#fff"/></svg>
    </div>
  </div>
  <div class="abs dots"><i></i><i class="on"></i><i></i></div>
</section>

<section class="cta">
  <div class="cta-photo" role="img" aria-label="Evening terrace restaurant beside a lit swimming pool"></div>
  <div class="abs cta-box">
    <p>You're Looking For The Best Quality And Peace Of Mind On Your Wedding Day, Then You're In The Right Place</p>
    <span class="btn">Book your wedding or event now !</span>
  </div>
</section>

<section class="blog" id="blog">
  <h2 class="section-title" style="top:58px">LATEST <span>BLOG</span></h2>
  <div class="rule" style="left:133px;top:128px;width:934px"></div>
  <svg class="abs arrow" style="left:86px" width="22" height="40" viewBox="0 0 22 40"><path d="M18 2L4 20L18 38" stroke="#cfcfcf" stroke-width="3" fill="none"/></svg>
  <svg class="abs arrow" style="left:1092px" width="22" height="40" viewBox="0 0 22 40"><path d="M4 2L18 20L4 38" stroke="#cfcfcf" stroke-width="3" fill="none"/></svg>
  <article class="abs post post-1" style="left:133px">
    <div class="post-photo" role="img" aria-label="Elegant reception table setting with glassware"></div>
    <div class="post-body"><h4>Uis nostrud exercitation an ullamco</h4><div class="post-meta">By Dane &nbsp;|&nbsp; Nov 02, 2017</div><p>Ut enim ad minim veniam, quis nostrud exercitation an ullamco laboris nisi ut</p><span class="btn">Read more</span></div>
  </article>
  <article class="abs post post-2" style="left:453px">
    <div class="post-photo" role="img" aria-label="Couple holding hands at a formal event"></div>
    <div class="post-body"><h4>Uis nostrud exercitation an ullamco</h4><div class="post-meta">By Dane &nbsp;|&nbsp; Nov 02, 2017</div><p>Ut enim ad minim veniam, quis nostrud exercitation an ullamco laboris nisi ut</p><span class="btn">Read more</span></div>
  </article>
  <article class="abs post post-3" style="left:772px">
    <div class="post-photo" role="img" aria-label="Garden estate venue with cypress trees"></div>
    <div class="post-body"><h4>Uis nostrud exercitation an ullamco</h4><div class="post-meta">By Dane &nbsp;|&nbsp; Nov 02, 2017</div><p>Ut enim ad minim veniam, quis nostrud exercitation an ullamco laboris nisi ut</p><span class="btn">Read more</span></div>
  </article>
</section>

<section class="contact" id="contact" role="img" aria-label="Dim candlelit evening scene behind the contact form">
  <h2 class="section-title">CONTACT US</h2>
  <div class="rule" style="left:133px;top:127px;width:934px;background:rgba(255,255,255,.25)"></div>
  <div class="abs contact-panel">
    <div class="contact-info">Email: hello@danemorrowfilms.example<br>Phone: (555) 014-7290</div>
    <div class="field" style="left:40px;top:130px;width:318px;height:40px">Name*</div>
    <div class="field" style="left:366px;top:130px;width:322px;height:40px">Email*</div>
    <div class="field" style="left:40px;top:178px;width:648px;height:126px">Message*</div>
    <span class="btn btn-outline">Read more</span>
  </div>
  <div class="abs contact-icon">
    <svg width="58" height="58" viewBox="0 0 58 58"><path d="M18 29L40 19L33 41L29 32Z" fill="none" stroke="#333" stroke-width="2" stroke-linejoin="round"/><path d="M29 32L40 19" stroke="#333" stroke-width="2"/></svg>
  </div>
</section>

<footer class="site-footer">Copyright © 2017 Dane Morrow Films. All Rights Reserved</footer>

</body>
</html>
```